Business Cards Design for the electrical wholesaler: clean bold dynamic :)

We need a business card design that would follow our latest brand guidelines. As an electrical wholesaler we want to bring a fresh look and feel into the industry. The design should be clean bold and dynamic. It should come alive with the renewed energy of our green colour. Our grey colour should keep things balanced and complement the notion of maturity and responsibility. We employ Lato as a corporate font however are not bound by this font and we’re open to interpretation here.

Target Market(s)

Electrical contractors

Industry/Entity Type

Business

Contact Information for Business Card

Logo
Name & Surname: Olena Dovbush
Job Title: Director of Marketing
Email: helen.dovbush@mailvane.example
Cell phone: XXX.XXX.XXXX
Address: 20917 - 87 Ave. Edmonton, AB, Canada. T6K 2R8
Business Phone: 780.555.0187
Website: www.qorvil.example

Font styles to use
Other font styles liked:
• Lato

Requirements
Must have
• Logo & website
Nice to have
• Brand elements - some of them you may find in the attached Brand Guidelines (e.g. three lines on the background signifying "W")

```html
<!DOCTYPE html>
<html lang="en">
<head>
<meta charset="utf-8">
<title>Qorvil Business Cards</title>
<link href="https://fonts.googleapis.com/css2?family=Lato:wght@300;400;700&display=swap" rel="stylesheet">
<style>
  :root {
    --stage: #e9ecef;
    --card: #ffffff;
    --brand-green: #8dc63f;
    --brand-grey: #58595b;
    --ink: #2d2f4a;
    --ink-soft: #55566a;
    --icon: #3a3b4a;
  }
  * { margin: 0; padding: 0; box-sizing: border-box; }
  html, body { width: 1200px; height: 1000px; overflow: hidden; }
  body {
    background: var(--stage);
    font-family: "Lato", sans-serif;
    position: relative;
  }
  .card {
    position: absolute;
    background: var(--card);
    overflow: hidden;
  }
  .card--rounded { border-radius: 30px; }
  .card--front-rounded { left: 64px; top: 60px; width: 508px; height: 290px; }
  .card--back-rounded  { left: 62px; top: 428px; width: 510px; height: 290px; }
  .card--front-square  { left: 624px; top: 283px; width: 513px; height: 292px; }
  .card--back-square   { left: 624px; top: 638px; width: 512px; height: 292px; }

  .wordmark {
    position: absolute;
    display: flex;
    align-items: center;
    color: var(--brand-grey);
    font-weight: 700;
    letter-spacing: -0.5px;
    line-height: 1;
  }
  .wordmark__square {
    background: var(--brand-green);
    flex: none;
  }
  .card__front-mark {
    left: 50%; top: 50%;
    transform: translate(-50%, -50%);
    font-size: 64px;
    gap: 16px;
  }
  .card__front-mark .wordmark__square { width: 50px; height: 50px; }

  .card__back-mark {
    right: 32px; top: 38px;
    font-size: 42px;
    gap: 10px;
  }
  .card__back-mark .wordmark__square { width: 32px; height: 32px; }

  .person {
    position: absolute;
    left: 28px; top: 80px;
  }
  .person__name {
    font-size: 26px;
    font-weight: 400;
    color: var(--ink);
    line-height: 1.1;
  }
  .person__title {
    margin-top: 6px;
    font-size: 15px;
    font-weight: 400;
    color: var(--ink-soft);
  }

  .contact-band {
    position: absolute;
    left: 0; right: 0; bottom: 0;
    height: 144px;
    background: var(--brand-green);
    color: var(--ink);
  }
  .contact-list {
    position: absolute;
    left: 30px; top: 36px;
    list-style: none;
    font-size: 17px;
  }
  .contact-list li {
    display: flex;
    align-items: center;
    gap: 11px;
    height: 24px;
  }
  .contact-list svg { width: 13px; height: 13px; fill: var(--icon); flex: none; }

  .address {
    position: absolute;
    right: 30px; top: 4px;
    text-align: right;
    font-size: 15.5px;
    line-height: 19px;
    font-style: normal;
  }
  .address__line--first svg {
    width: 11px; height: 14px; fill: var(--icon);
    vertical-align: -1px; margin-right: 5px;
  }
  .website {
    position: absolute;
    right: 34px; bottom: 26px;
    font-size: 15px;
  }
</style>
</head>
<body>

  <section class="card card--rounded card--front-rounded">
    <div class="wordmark card__front-mark"><span class="wordmark__square"></span>qorvil</div>
  </section>

  <section class="card card--rounded card--back-rounded">
    <div class="wordmark card__back-mark"><span class="wordmark__square"></span>qorvil</div>
    <div class="person">
      <h1 class="person__name">Olena Dovbush</h1>
      <p class="person__title">Director of Marketing</p>
    </div>
    <div class="contact-band">
      <address class="address">
        <span class="address__line--first"><svg viewBox="0 0 12 16"><path d="M6 0a6 6 0 0 0-6 6c0 4.5 6 10 6 10s6-5.5 6-10a6 6 0 0 0-6-6zm0 8.5A2.5 2.5 0 1 1 6 3.5a2.5 2.5 0 0 1 0 5z"/></svg>20917 - 87 Ave.</span><br>
        Edmonton, AB,<br>
        Canada. T6K 2R8
      </address>
      <ul class="contact-list">
        <li><svg viewBox="0 0 16 16"><path d="M3.6 0.5l2.4 3.2-1.4 1.9c.9 2 2.6 3.8 4.8 4.8l1.9-1.4 3.2 2.4-1.2 3.1C7.8 14.6 1.4 8.2 0.5 1.7z"/></svg>780.555.0187</li>
        <li><svg viewBox="0 0 16 16"><path d="M1 5C1 2 15 2 15 5v1.5h-3.5V5h-7v1.5H1zM4 8h8l2 6H2zm4 1.5a2 2 0 1 0 0 4 2 2 0 0 0 0-4z"/></svg>780.555.0187</li>
        <li><svg viewBox="0 0 16 16"><path d="M1 3h14v1.2L8 8.8 1 4.2zm0 2.8l7 4.6 7-4.6V13H1z"/></svg>helen.dovbush@mailvane.example</li>
      </ul>
      <p class="website">www.qorvil.example</p>
    </div>
  </section>

  <section class="card card--front-square">
    <div class="wordmark card__front-mark"><span class="wordmark__square"></span>qorvil</div>
  </section>

  <section class="card card--back-square">
    <div class="wordmark card__back-mark"><span class="wordmark__square"></span>qorvil</div>
    <div class="person">
      <h2 class="person__name">Olena Dovbush</h2>
      <p class="person__title">Director of Marketing</p>
    </div>
    <div class="contact-band">
      <address class="address">
        <span class="address__line--first"><svg viewBox="0 0 12 16"><path d="M6 0a6 6 0 0 0-6 6c0 4.5 6 10 6 10s6-5.5 6-10a6 6 0 0 0-6-6zm0 8.5A2.5 2.5 0 1 1 6 3.5a2.5 2.5 0 0 1 0 5z"/></svg>20917 - 87 Ave.</span><br>
        Edmonton, AB,<br>
        Canada. T6K 2R8
      </address>
      <ul class="contact-list">
        <li><svg viewBox="0 0 16 16"><path d="M3.6 0.5l2.4 3.2-1.4 1.9c.9 2 2.6 3.8 4.8 4.8l1.9-1.4 3.2 2.4-1.2 3.1C7.8 14.6 1.4 8.2 0.5 1.7z"/></svg>780.555.0187</li>
        <li><svg viewBox="0 0 16 16"><path d="M1 5C1 2 15 2 15 5v1.5h-3.5V5h-7v1.5H1zM4 8h8l2 6H2zm4 1.5a2 2 0 1 0 0 4 2 2 0 0 0 0-4z"/></svg>780.555.0187</li>
        <li><svg viewBox="0 0 16 16"><path d="M1 3h14v1.2L8 8.8 1 4.2zm0 2.8l7 4.6 7-4.6V13H1z"/></svg>helen.dovbush@mailvane.example</li>
      </ul>
      <p class="website">www.qorvil.example</p>
    </div>
  </section>

</body>
</html>
```